Cover for a recovery from breast augmentation surgery pamphlet

Need a cover which includes my logo for new pamphlet on recovering from breast augmentation surgery It is just a quick how to guide.
I would like the cover to incorporate the Borela logo(2 options given) and be simple and clean. Will require in a vector file as well.

The title:
Well, Your Chest Is Upgraded...
WHAT NEXT?!

By: Borela

A little about me: I am an adult industry writer and am looking to do a mainstream project. This is a project I want to appeal to mainstream women.

Target Market(s)

Women who are recovering from or entertaining breast augmentation surgery

Font styles to use
Serif

Requirements
Must have
• One Borela logo, titile, and by Borela
Nice to have
• i love modern clean sleek design that is easy to read
Should not have
• nothing that would offend women or make them uncomfortable about their body

```html
<!DOCTYPE html>
<html lang="en">
<head>
<meta charset="utf-8">
<title>Borela – Recovery Guide Cover</title>
<link rel="stylesheet" href="https://fonts.googleapis.com/css2?family=PT+Serif:wght@400;700&family=Oswald:wght@500&family=Lato:wght@400&display=swap">
<style>
  :root {
    --magenta: #c0277f;
    --magenta-soft: #d45a9e;
    --slate: #6b6b6b;
    --ink: #2b2b2b;
    --paper: #ffffff;
    --backdrop: #7a4b26;
    --scrub-blue: #8fb4d9;
    --scrub-light: #cfdded;
    --mist: #e4e4e6;
  }
  * { margin: 0; padding: 0; box-sizing: border-box; }
  html, body { width: 1200px; height: 907px; overflow: hidden; }
  body { background: var(--backdrop); position: relative; font-family: "Lato", sans-serif; }

  .pamphlet { position: absolute; left: 124px; top: 111px; width: 955px; height: 680px; display: flex; }

  /* back cover */
  .back-cover { position: relative; width: 476px; height: 680px; background: var(--paper); overflow: hidden; }
  .back-cover__photo-top {
    position: absolute; left: 0; top: 0; width: 100%; height: 230px;
    background: linear-gradient(to bottom, #d9dadd 0%, #ececee 60%, var(--paper) 100%);
  }
  .back-cover__photo-bottom {
    position: absolute; left: 0; bottom: 0; width: 100%; height: 280px;
    background: linear-gradient(to top, #dcdcde 0%, #ededee 55%, var(--paper) 100%);
  }
  .back-cover__brand {
    position: absolute; left: 0; top: 248px; width: 100%; text-align: center;
    font-family: "PT Serif", serif; font-weight: 700; font-size: 54px; color: var(--magenta);
  }
  .back-cover__web {
    position: absolute; left: 0; top: 381px; width: 100%; text-align: center;
    font-size: 17px; color: var(--ink);
  }

  /* front cover */
  .front-cover { position: relative; width: 479px; height: 680px; background: var(--paper); overflow: hidden; }
  .front-cover__photo {
    position: absolute; left: 0; top: 0; width: 100%; height: 420px;
    background: linear-gradient(135deg, var(--scrub-light) 0%, var(--scrub-blue) 45%, #b7cbe0 75%, var(--mist) 100%);
  }
  .front-cover__shapes { position: absolute; left: 0; top: 0; }
  .front-cover__brand {
    position: absolute; left: 0; top: 52px; width: 100%; text-align: center;
    font-family: "PT Serif", serif; font-weight: 700; font-size: 54px; color: var(--paper);
  }
  .title { position: absolute; left: 0; top: 430px; width: 100%; text-align: center; }
  .title__lead {
    display: block; font-family: "PT Serif", serif; font-weight: 700;
    font-size: 38px; color: var(--magenta); line-height: 44px;
  }
  .title__main {
    display: block; font-family: "Oswald", sans-serif; font-weight: 500;
    font-size: 52px; color: var(--slate); line-height: 68px; letter-spacing: 1px;
  }
  .title__ask {
    position: absolute; left: 52px; top: 555px; width: 380px; height: 52px;
    background: var(--slate); border-radius: 8px;
    font-family: "PT Serif", serif; font-size: 34px; color: var(--paper);
    display: flex; align-items: center; justify-content: center; letter-spacing: 1px;
  }
  .front-cover__web {
    position: absolute; left: 0; top: 624px; width: 100%; text-align: center;
    font-size: 17px; letter-spacing: 2px; color: var(--ink);
  }
</style>
</head>
<body>
  <main class="pamphlet">
    <section class="back-cover">
      <div class="back-cover__photo-top" role="img" aria-label="Faded photo of a surgical team at work in an operating room"></div>
      <div class="back-cover__photo-bottom" role="img" aria-label="Faded photo of surgical instruments laid out on a tray"></div>
      <div class="back-cover__brand">Borela</div>
      <div class="back-cover__web">www.borelaguide.com</div>
    </section>

    <section class="front-cover">
      <div class="front-cover__photo" role="img" aria-label="Photo of a smiling surgeon in blue scrubs with a surgical team in the background"></div>
      <svg class="front-cover__shapes" width="479" height="680" viewBox="0 0 479 680" aria-hidden="true">
        <ellipse cx="240" cy="18" rx="272" ry="146" fill="var(--paper)"/>
        <ellipse cx="240" cy="14" rx="262" ry="138" fill="var(--magenta)"/>
        <path d="M0,418 Q240,338 479,404 L479,680 L0,680 Z" fill="var(--paper)"/>
        <path d="M0,412 Q240,332 479,398" fill="none" stroke="var(--magenta)" stroke-width="9"/>
      </svg>
      <div class="front-cover__brand">Borela</div>
      <h1 class="title">
        <span class="title__lead">WELL, YOUR CHEST</span>
        <span class="title__main">IS UPGRADED...</span>
      </h1>
      <div class="title__ask">WHAT NEXT?!</div>
      <div class="front-cover__web">www.borelaguide.com</div>
    </section>
  </main>
</body>
</html>
```